Tavlor Suite Background image creation.

We need someone to develop an image that is 1920x1080 using our company logo and and colors. We will be using this as the login page background on tavlorsuite.net for all our clients.

```html
<!DOCTYPE html>
<html lang="en">
<head>
<meta charset="utf-8">
<title>Tavlor Suite – Login Background</title>
<link rel="stylesheet" href="https://fonts.googleapis.com/css2?family=Exo+2:wght@600&display=swap">
<style>
  :root {
    --sky-base: #1496d3;
    --sky-deep: #0a8bcc;
    --sky-light: #3fb0e2;
    --bubble-edge: #2d9fdc;
    --glow-white: #ffffff;
    --brand-blue: #1b8fd1;
  }
  html, body {
    margin: 0;
    padding: 0;
    width: 1200px;
    height: 675px;
    overflow: hidden;
    background: var(--sky-base);
  }
  .login-backdrop {
    position: relative;
    width: 1200px;
    height: 675px;
    overflow: hidden;
  }
  .backdrop-art {
    position: absolute;
    inset: 0;
    display: block;
  }
  .brand-mark {
    position: absolute;
    top: 78px;
    left: 862px;
    display: flex;
    align-items: center;
    gap: 14px;
  }
  .brand-dot {
    width: 30px;
    height: 30px;
    border-radius: 50%;
    background: var(--brand-blue);
  }
  .brand-name {
    margin: 0;
    font-family: "Exo 2", sans-serif;
    font-weight: 600;
    font-size: 34px;
    line-height: 1;
    letter-spacing: 0.5px;
    color: var(--brand-blue);
  }
</style>
</head>
<body>
<main class="login-backdrop">
  <svg class="backdrop-art" viewBox="0 0 1200 675" width="1200" height="675" aria-hidden="false">
    <defs>
      <linearGradient id="sky-fill" x1="0" y1="0" x2="1" y2="1">
        <stop offset="0" stop-color="var(--sky-light)"/>
        <stop offset="0.5" stop-color="var(--sky-base)"/>
        <stop offset="1" stop-color="var(--sky-deep)"/>
      </linearGradient>
      <radialGradient id="network-haze" cx="0.35" cy="0.5" r="0.6">
        <stop offset="0" stop-color="#ffffff" stop-opacity="0.07"/>
        <stop offset="1" stop-color="#ffffff" stop-opacity="0"/>
      </radialGradient>
      <radialGradient id="bubble-upper" cx="0.78" cy="0.18" r="0.85">
        <stop offset="0" stop-color="#ffffff"/>
        <stop offset="0.3" stop-color="#d6eefa"/>
        <stop offset="0.6" stop-color="#6cc4ec"/>
        <stop offset="1" stop-color="var(--bubble-edge)"/>
      </radialGradient>
      <radialGradient id="bubble-lower" cx="0.55" cy="0.1" r="0.9">
        <stop offset="0" stop-color="#ffffff" stop-opacity="0.95"/>
        <stop offset="0.3" stop-color="#9ad8f3"/>
        <stop offset="0.65" stop-color="#3aa8e0"/>
        <stop offset="1" stop-color="#1e8fd4"/>
      </radialGradient>
      <radialGradient id="corner-glow" cx="0.5" cy="0.5" r="0.5">
        <stop offset="0" stop-color="var(--glow-white)" stop-opacity="1"/>
        <stop offset="0.55" stop-color="var(--glow-white)" stop-opacity="0.6"/>
        <stop offset="1" stop-color="var(--glow-white)" stop-opacity="0"/>
      </radialGradient>
    </defs>

    <rect class="sky" x="0" y="0" width="1200" height="675" fill="url(#sky-fill)"/>
    <rect class="network-pattern" x="0" y="0" width="1200" height="675" fill="url(#network-haze)"
          role="img" aria-label="Faint pattern of connected network nodes and lines"/>

    <circle class="bubble bubble-upper" cx="902" cy="190" r="330" fill="url(#bubble-upper)" opacity="0.95"/>
    <circle class="bubble bubble-lower" cx="1128" cy="570" r="350" fill="url(#bubble-lower)" opacity="0.9"/>
    <ellipse class="corner-glow" cx="1010" cy="110" rx="230" ry="150" fill="url(#corner-glow)"/>
  </svg>

  <div class="brand-mark">
    <span class="brand-dot"></span>
    <p class="brand-name">Corvane Systems</p>
  </div>
</main>
</body>
</html>
```